Flyer Design Project with menu

We are from Copperleaf Kitchen Restaurant. We usually serve breakfast, soul food, fried and BBQ Ribs , legs, wings etc. We located at 2738 n. Willow avenue, canton, 39046, MS. Since this is a new restaurant we want to let people know about us. Please create a good professional flyer including menu on that. Thank you. Please let us know if you need any other information.

Target Market(s)

We want to attract customers from 3 different locations near 15 miles radius.

Industry/Entity Type

American Restaurant

Font styles to use
Serif

Requirements
Must have
• Good graphics with food pictures.
• Soul food graphic pictures, RIBS, FISH and breakfast regular.
Nice to have
• 20% discount coupon offer.

```html
<!DOCTYPE html>
<html lang="en">
<head>
<meta charset="utf-8">
<title>Copperleaf Kitchen Restaurant – Trifold Flyer</title>
<link rel="stylesheet" href="https://fonts.googleapis.com/css2?family=Cinzel:wght@400;700&family=Oswald:wght@400;500&family=Roboto+Condensed:ital,wght@0,500;0,700;1,500&family=Roboto:wght@700;900&display=swap">
<style>
  :root {
    --red: #c4321f;
    --red-deep: #b22a18;
    --yellow: #fcd43c;
    --gold-text: #fbd23a;
    --ink: #3a1a10;
    --black: #1d1d1d;
    --white: #ffffff;
    --coupon-red: #d42a25;
  }
  * { margin: 0; padding: 0; box-sizing: border-box; }
  html, body { width: 1200px; height: 854px; overflow: hidden; background: var(--white); }
  .flyer { position: relative; width: 1200px; height: 854px; overflow: hidden; }
  .panel { position: absolute; top: 0; height: 854px; }
  .panel--offer { left: 0; width: 405px; background: var(--red); }
  .panel--contact { left: 405px; width: 395px; background: var(--white); }
  .panel--cover { left: 800px; width: 400px; background: linear-gradient(160deg, var(--red) 0%, var(--red-deep) 100%); }

  .photo { position: absolute; }
  .photo--kebab { left: 0; top: 0; width: 405px; height: 226px; background: linear-gradient(135deg, #5a1d0c 0%, #8a2e12 45%, #e0721c 80%, #f4a42a 100%); }
  .photo--ribs { left: 0; top: 0; width: 400px; height: 320px; background: linear-gradient(160deg, #3a2418 0%, #9a3a16 45%, #d6561c 75%, #c4321f 100%); }
  .photo--dish { width: 112px; height: 112px; border-radius: 50%; border: 3px solid var(--white); top: 290px; }
  .dish-1 { left: 15px; background: radial-gradient(circle, #d8b48a, #8a4a2a); }
  .dish-2 { left: 142px; background: radial-gradient(circle, #e8dcc0, #b07a3a); }
  .dish-3 { left: 270px; background: radial-gradient(circle, #e2a040, #9a4a14); }

  .offer-title { position: absolute; left: 0; width: 405px; top: 258px; text-align: center; color: var(--white); font-family: "Cinzel", serif; font-size: 34px; line-height: 44px; white-space: nowrap; text-shadow: 1px 2px 2px rgba(0,0,0,.35); }
  .offer-discount { position: absolute; left: 50px; top: 410px; color: var(--white); font-family: "Cinzel", serif; text-shadow: 1px 2px 2px rgba(0,0,0,.35); white-space: nowrap; }
  .offer-discount .get { font-size: 36px; vertical-align: top; position: relative; top: 8px; }
  .offer-discount .num { font-size: 96px; line-height: 1; }
  .offer-discount .off { font-size: 40px; }

  .scissors { position: absolute; left: 40px; top: 566px; }
  .coupon { position: absolute; left: 38px; top: 588px; width: 330px; height: 233px; background: var(--white); border: 2px dashed #999; }
  .coupon-name { margin-top: 18px; text-align: center; font-family: "Oswald", sans-serif; font-size: 21px; color: var(--black); letter-spacing: -.3px; white-space: nowrap; }
  .coupon-bar { margin-top: 8px; background: var(--black); color: var(--white); text-align: center; font-family: "Roboto Condensed", sans-serif; font-weight: 500; font-size: 22px; height: 37px; line-height: 37px; }
  .coupon-value { text-align: center; color: var(--coupon-red); font-family: "Roboto", sans-serif; font-weight: 900; margin-top: 2px; white-space: nowrap; }
  .coupon-value .pct { font-size: 50px; }
  .coupon-value .num { font-size: 104px; line-height: 112px; letter-spacing: -2px; }
  .coupon-value .off { font-size: 34px; font-weight: 700; }
  .coupon-note { position: absolute; left: 8px; right: 8px; bottom: 8px; background: var(--black); color: var(--white); text-align: center; font-family: "Roboto", sans-serif; font-size: 11px; height: 18px; line-height: 18px; letter-spacing: .5px; }

  .brand { position: absolute; display: flex; align-items: center; gap: 10px; font-family: "Oswald", sans-serif; font-weight: 400; text-transform: uppercase; line-height: 1.05; text-align: center; }
  .brand-mark { width: 14px; height: 14px; background: var(--yellow); flex: none; }
  .brand--contact { left: 0; width: 395px; justify-content: center; top: 270px; font-size: 32px; color: var(--ink); }
  .brand--cover { left: 22px; top: 28px; font-size: 30px; color: var(--white); text-shadow: 0 1px 3px rgba(0,0,0,.5); }

  .tagline { font-family: "Roboto Condensed", sans-serif; font-style: italic; font-weight: 500; }
  .tagline--contact { position: absolute; left: 0; width: 395px; top: 433px; text-align: center; font-size: 16px; color: var(--ink); }
  .contact-list { position: absolute; left: 50px; top: 560px; list-style: none; font-family: "Oswald", sans-serif; font-weight: 500; font-size: 17px; color: var(--ink); }
  .contact-list li { display: flex; align-items: center; height: 34px; }
  .contact-list svg { width: 26px; margin-right: 10px; }

  .cover-title { position: absolute; left: 0; width: 400px; top: 436px; text-align: center; font-family: "Cinzel", serif; font-size: 33px; line-height: 38px; white-space: nowrap; color: var(--gold-text); text-shadow: 1px 2px 2px rgba(0,0,0,.4); }
  .cover-hours { position: absolute; left: 0; width: 400px; top: 534px; text-align: center; font-family: "Cinzel", serif; font-size: 17px; color: var(--white); letter-spacing: .3px; }
  .menu-list { position: absolute; left: 40px; top: 592px; list-style: none; font-family: "Cinzel", serif; font-size: 20px; line-height: 20px; color: var(--white); white-space: nowrap; }
  .menu-list li { display: flex; align-items: center; gap: 8px; }
  .menu-list svg { width: 14px; height: 14px; }
  .tagline--cover { position: absolute; right: 33px; top: 679px; font-size: 17px; color: var(--white); }
  .call-band { position: absolute; left: 0; top: 772px; width: 400px; height: 70px; }
  .call-text { position: absolute; left: 0; width: 400px; top: 790px; display: flex; justify-content: center; align-items: center; gap: 10px; font-family: "Oswald", sans-serif; font-weight: 500; font-size: 24px; color: var(--ink); }
  .bottom-strip { position: absolute; left: 0; top: 842px; width: 400px; height: 12px; background: var(--red); }
</style>
</head>
<body>
<main class="flyer">

  <section class="panel panel--offer">
    <div class="photo photo--kebab" role="img" aria-label="Grilled kebab skewers over a flaming grill"></div>
    <h2 class="offer-title">At<br>Copperleaf Kitchen<br>Restaurant</h2>
    <p class="offer-discount"><span class="get">GET</span><span class="num">20</span><span class="off">%OFF</span></p>
    <svg class="scissors" width="62" height="34" viewBox="0 0 62 34" aria-hidden="true">
      <circle cx="9" cy="9" r="6.5" fill="none" stroke="#1d1d1d" stroke-width="3.5"/>
      <circle cx="9" cy="26" r="6.5" fill="none" stroke="#1d1d1d" stroke-width="3.5"/>
      <path d="M14 12 L60 30 M14 23 L60 4" stroke="#1d1d1d" stroke-width="4" stroke-linecap="round"/>
    </svg>
    <div class="coupon">
      <p class="coupon-name">COPPERLEAF KITCHEN RESTAURANT</p>
      <p class="coupon-bar">exclusive coupon just for you</p>
      <p class="coupon-value"><span class="pct">%</span><span class="num">20</span><span class="off">off</span></p>
      <p class="coupon-note">Bring this coupon with you and get 10% off!</p>
    </div>
  </section>

  <section class="panel panel--contact">
    <div class="brand brand--contact"><span class="brand-mark"></span><span>Copperleaf<br>Kitchen<br>Restaurant</span></div>
    <p class="tagline tagline--contact">We serve best soul food in canton!</p>
    <ul class="contact-list">
      <li><svg viewBox="0 0 24 24" height="24"><path d="M7 2c1 0 2 3 2.5 4.5.3 1-1.5 2-1.5 3 0 2 2 6 4 7.5.8.6 2-1 3-.8 1.5.4 3.5 2 3.5 3s-2 3-4 2.8C8 21 3 12 3.5 6 3.7 4 5.5 2 7 2z" fill="#3a1a10"/></svg>7695550148</li>
      <li><svg viewBox="0 0 26 18" height="16"><rect x="1" y="1" width="24" height="16" fill="none" stroke="#3a1a10" stroke-width="2"/><path d="M1 1 L13 10 L25 1 M1 17 L10 8 M25 17 L16 8" fill="none" stroke="#3a1a10" stroke-width="2"/></svg>hello@copperleafkitchen.com</li>
      <li><svg viewBox="0 0 24 26" height="24"><path d="M12 1a8 8 0 0 0-8 8c0 6 8 16 8 16s8-10 8-16a8 8 0 0 0-8-8z" fill="#3a1a10"/><circle cx="12" cy="9" r="3.2" fill="#fff"/></svg>2738 n. Willow avenue, canton, 39046, MS</li>
    </ul>
  </section>

  <section class="panel panel--cover">
    <div class="photo photo--ribs" role="img" aria-label="Barbecue ribs with grilled peppers on a smoking grill"></div>
    <div class="photo photo--dish dish-1" role="img" aria-label="Plate of ham, biscuits and greens"></div>
    <div class="photo photo--dish dish-2" role="img" aria-label="Plate of fried chicken, mashed potatoes and coleslaw"></div>
    <div class="photo photo--dish dish-3" role="img" aria-label="Plate of fried fish"></div>
    <div class="brand brand--cover"><span class="brand-mark"></span><span>Copperleaf<br>Kitchen<br>Restaurant</span></div>
    <h1 class="cover-title">Copperleaf Kitchen<br>Restaurant</h1>
    <p class="cover-hours">SERVING BREAKFAST, LUNCH &amp; DINNER</p>
    <ul class="menu-list">
      <li><svg viewBox="0 0 24 24"><path d="M12 1l3.2 7 7.6.8-5.7 5.1 1.6 7.5L12 17.6 5.3 21.4l1.6-7.5L1.2 8.8 8.8 8z" fill="#fcd43c"/></svg>BREAKFAST</li>
      <li><svg viewBox="0 0 24 24"><path d="M12 1l3.2 7 7.6.8-5.7 5.1 1.6 7.5L12 17.6 5.3 21.4l1.6-7.5L1.2 8.8 8.8 8z" fill="#fcd43c"/></svg>SOUL FOOD</li>
      <li><svg viewBox="0 0 24 24"><path d="M12 1l3.2 7 7.6.8-5.7 5.1 1.6 7.5L12 17.6 5.3 21.4l1.6-7.5L1.2 8.8 8.8 8z" fill="#fcd43c"/></svg>FRIED &amp; BBQ RIBS, LEGS, WINGGS</li>
    </ul>
    <p class="tagline tagline--cover">We serve best soul food in canton!</p>
    <svg class="call-band" viewBox="0 0 400 70" preserveAspectRatio="none" aria-hidden="true">
      <path d="M0 6 L6 0 L12 6 L18 0 L24 6 L30 0 L36 6 L42 0 L48 6 L54 0 L60 6 L66 0 L72 6 L78 0 L84 6 L90 0 L96 6 L102 0 L108 6 L114 0 L120 6 L126 0 L132 6 L138 0 L144 6 L150 0 L156 6 L162 0 L168 6 L174 0 L180 6 L186 0 L192 6 L198 0 L204 6 L210 0 L216 6 L222 0 L228 6 L234 0 L240 6 L246 0 L252 6 L258 0 L264 6 L270 0 L276 6 L282 0 L288 6 L294 0 L300 6 L306 0 L312 6 L318 0 L324 6 L330 0 L336 6 L342 0 L348 6 L354 0 L360 6 L366 0 L372 6 L378 0 L384 6 L390 0 L396 6 L400 2 L400 70 L0 70 Z" fill="#fcd43c"/>
    </svg>
    <p class="call-text"><svg viewBox="0 0 24 24" width="24" height="30"><path d="M7 2c1 0 2 3 2.5 4.5.3 1-1.5 2-1.5 3 0 2 2 6 4 7.5.8.6 2-1 3-.8 1.5.4 3.5 2 3.5 3s-2 3-4 2.8C8 21 3 12 3.5 6 3.7 4 5.5 2 7 2z" fill="#3a1a10"/></svg>Call Now : 7695550148</p>
    <div class="bottom-strip"></div>
  </section>

</main>
</body>
</html>
```